Behind the Scenes Created for a Wedding Photography - Cinematic Film Poster (Hollywood Style)

We require a Film Poster to be created in launch of a new Film that is launching early next week. We are looking for a very cinematic look to the poster as you would see for any hollywood film.
This poster will be printed A3 for advertsing.
We want a few photos blended together.

Film:

We shot a Pre Wedding Shoot in Florance and have done a behind the Scenes video for the photographer. The photographer will be sharing the video with his clients on his FB page and need this poster to promote the video.

We would like the text on the poster as hollywood films do. The tight small writing with the following information:

Torvel Studios Presents a Jory Tesken Film Edited by Jory Tesken Director of Photography by Jory Tesken Produced by Devan Olrick Executive Producer Jory Tesken Filmed in 16:9 Widescreen Cinematography Jory Tesken Shot entirley on location in Florance

Title - The Quiet Lantern

A film by Jory Tesken

We would also like the images blended together.

I have had to compress the images as it wouldnt allow me to upload the full res images onto Plexa Hub but I assume for the final design we will have to send full res images?

Also we require the .PSD file with all the layers clearly labelled and structured so we can make minor tweaks ourselves if required.

Thanks

Target Market(s)

Wedding Bride and Grooms.

Industry/Entity Type

Wedding Photography

Font styles to use
Serif

Requirements
Must have
• Images Merged in a cinematic style.
• The writing at the bottom in a certain style font that allows it to look like a hollywood poster.
• The poster is for a photographer - "Devan Photography" ( I have uploaded his Logo)
• Have the release date as 25.12.2015
Nice to have
• n/a
Should not have
• Should not look cheesy and needs to look as professional cinematic.

```html
<!DOCTYPE html>
<html lang="en">
<head>
<meta charset="utf-8">
<title>The Quiet Lantern – Film Poster</title>
<link rel="stylesheet" href="https://fonts.googleapis.com/css2?family=Bodoni+Moda:ital,opsz,wght@0,6..96,400;1,6..96,400&display=swap">
<style>
  :root {
    --sky-deep: #26313d;
    --sky-storm: #48515a;
    --sky-blue: #1f55a8;
    --cloud-light: #c3c8cc;
    --stone-light: #8a8178;
    --stone-mid: #5f574f;
    --stone-dark: #2e2a26;
    --pavement: #34322f;
    --title-white: #ffffff;
    --credit-grey: rgba(228, 228, 228, 0.78);
    --brand-white: #f2f0ec;
  }
  * { margin: 0; padding: 0; box-sizing: border-box; }
  html, body {
    width: 852px;
    height: 1200px;
    overflow: hidden;
    background: #111;
  }
  .poster {
    position: relative;
    width: 852px;
    height: 1200px;
    overflow: hidden;
    font-family: "Bodoni Moda", Georgia, serif;
  }
  .poster__photo {
    position: absolute;
    inset: 0;
    background:
      linear-gradient(180deg, transparent 0 80%, rgba(30, 28, 26, 0.65) 88%, rgba(20, 19, 18, 0.9) 100%),
      radial-gradient(ellipse 110px 330px at 250px 820px, rgba(150, 160, 165, 0.55), transparent 75%),
      radial-gradient(ellipse 380px 300px at 560px 760px, var(--stone-light), transparent 80%),
      linear-gradient(100deg, var(--stone-dark) 0%, var(--stone-mid) 30%, transparent 55%),
      linear-gradient(180deg, transparent 0 30%, rgba(70, 64, 58, 0.9) 45%, var(--stone-mid) 65%, var(--pavement) 85%),
      radial-gradient(ellipse 260px 380px at 860px 380px, var(--sky-blue), transparent 75%),
      radial-gradient(ellipse 360px 180px at 580px 420px, var(--cloud-light), transparent 70%),
      radial-gradient(ellipse 260px 140px at 300px 120px, #6a7076, transparent 70%),
      linear-gradient(180deg, var(--sky-deep) 0%, var(--sky-storm) 40%, #5c6064 100%);
  }
  .poster__title {
    position: absolute;
    top: 22px;
    right: 50px;
    text-align: right;
    color: var(--title-white);
    font-style: italic;
    font-weight: 400;
    font-size: 98px;
    line-height: 128px;
  }
  .poster__title span { display: block; }
  .poster__byline {
    position: absolute;
    top: 296px;
    right: 62px;
    color: var(--title-white);
    font-style: italic;
    font-size: 12px;
  }
  .poster__credits {
    position: absolute;
    right: 52px;
    top: 1018px;
    text-align: right;
    color: var(--credit-grey);
    font-style: italic;
    font-size: 9px;
    line-height: 15.5px;
  }
  .poster__credits p { white-space: nowrap; }
  .poster__release {
    position: absolute;
    right: 52px;
    top: 1128px;
    color: var(--title-white);
    font-size: 15px;
    letter-spacing: 4px;
  }
  .poster__brand {
    position: absolute;
    left: 54px;
    top: 1104px;
    width: 104px;
    text-align: center;
    color: var(--brand-white);
    font-size: 11px;
    line-height: 14px;
    letter-spacing: 2.4px;
    text-transform: uppercase;
  }
</style>
</head>
<body>
  <main class="poster">
    <div class="poster__photo" role="img" aria-label="Blended photograph of an engaged couple embracing in front of Florence Cathedral's marble facade under a dramatic cloudy blue sky"></div>

    <h1 class="poster__title"><span>The Quiet</span><span>Lantern</span></h1>
    <p class="poster__byline">A film by Jory Tesken</p>

    <div class="poster__credits">
      <p>Torvel Studios Presents a Jory Tesken Film Edited by Jory Tesken</p>
      <p>Director of Photography by Jory Tesken</p>
      <p>Produced by Devan Olrick</p>
      <p>Executive Producer Jory Tesken</p>
      <p>Filmed in 16:9 Widescreen Cinematography</p>
      <p>Jory Tesken Shot entirely on location in Florence</p>
    </div>
    <p class="poster__release">25.12.2015</p>

    <p class="poster__brand">Devan<br>Photography</p>
  </main>
</body>
</html>
```